Business Card Design - R.T. Custom Cabinets Ltd.

Design a business card, including a new logo for a new company in Vancouver, British Columbia, Canada.

The logo must be available as a separate file.

The card should include all company information including:
R.T. Custom Cabinets Ltd.
5826 Larkspur Avenue
Burnaby, B.C. V7K 2P9
Telehone: 604-555-0173
Fax: 604-555-0173
www.rtcustomcabinets.example

As well as individual contact information for employees:
Name
Position
Telephone
Email

The card must include a thoughtful message as well

Target Market(s)

Custom Cabinets

Industry/Entity Type

Business

Contact Information for Business Card

Important information on the front, thoughtful message on the back

Colors
fbed22
9bcb3c
0355a3
ec1f27

Requirements
Must have
• See project description
Nice to have
• images that showcase custom cabinets (european, modern and traditional) styles

```html
<!DOCTYPE html>
<html lang="en">
<head>
<meta charset="utf-8">
<title>R.T. Custom Cabinets Ltd. – Business Card</title>
<link href="https://fonts.googleapis.com/css2?family=Open+Sans:ital,wght@0,400;0,700;1,400&display=swap" rel="stylesheet">
<style>
  :root {
    --page: #2b2b2b;
    --card: #1f2020;
    --green: #9bcb3c;
    --yellow: #fbed22;
    --blue: #0355a3;
    --red: #ec1f27;
    --white: #f2f2f2;
    --grey: #cfcfcf;
  }
  * { margin: 0; padding: 0; box-sizing: border-box; }
  html, body { width: 1200px; height: 900px; overflow: hidden; }
  body {
    background: var(--page);
    font-family: "Open Sans", Arial, sans-serif;
    position: relative;
  }
  .card {
    position: absolute;
    left: 285px;
    width: 630px;
    height: 360px;
    background: var(--card);
    border-radius: 22px;
    box-shadow: 0 10px 28px rgba(0,0,0,.45);
    overflow: hidden;
  }
  .card--back { top: 70px; }
  .card--front { top: 470px; }

  .wordmark {
    display: flex;
    align-items: center;
    gap: 14px;
    color: var(--green);
    font-weight: 400;
    white-space: nowrap;
  }
  .wordmark__square { background: var(--green); flex: none; }

  .back-content {
    position: absolute;
    left: 0; right: 0; top: 118px;
    display: flex;
    flex-direction: column;
    align-items: center;
  }
  .card--back .wordmark { font-size: 34px; letter-spacing: .04em; }
  .card--back .wordmark__square { width: 44px; height: 44px; }
  .message {
    margin-top: 22px;
    color: var(--grey);
    font-size: 16px;
    font-style: italic;
    text-align: center;
  }
  .palette {
    position: absolute;
    left: 0; right: 0; bottom: 0;
    height: 8px;
    display: flex;
  }
  .palette span { flex: 1; }
  .palette .p-green { background: var(--green); }
  .palette .p-yellow { background: var(--yellow); }
  .palette .p-blue { background: var(--blue); }
  .palette .p-red { background: var(--red); }

  .card--front .wordmark {
    position: absolute;
    right: 40px; top: 40px;
    font-size: 19px;
    letter-spacing: .03em;
  }
  .card--front .wordmark__square { width: 26px; height: 26px; }

  .person {
    position: absolute;
    left: 40px; top: 96px;
    padding-left: 16px;
    border-left: 7px solid var(--green);
  }
  .person__name {
    color: var(--white);
    font-size: 25px;
    font-weight: 400;
    line-height: 1.15;
  }
  .person__name strong { font-weight: 700; }
  .person__role { color: var(--green); font-size: 16px; line-height: 1.3; }

  .contacts {
    position: absolute;
    left: 70px; top: 178px;
    list-style: none;
    color: var(--grey);
    font-size: 14px;
    line-height: 1.35;
  }
  .contacts li {
    display: flex;
    align-items: flex-start;
    gap: 12px;
    margin-bottom: 6px;
  }
  .contacts svg { flex: none; margin-top: 2px; fill: var(--green); }
  .contacts .label { color: var(--green); }

  .rule {
    position: absolute;
    left: 60px; top: 330px;
    width: 270px; height: 3px;
    background: var(--green);
  }
  .website {
    position: absolute;
    right: 40px; top: 300px;
    color: var(--green);
    font-size: 16px;
  }
</style>
</head>
<body>

<section class="card card--back">
  <div class="back-content">
    <div class="wordmark"><span class="wordmark__square"></span>R.T. Custom Cabinets Ltd.</div>
    <p class="message">Crafted by hand, built to be the heart of your home.</p>
  </div>
  <div class="palette"><span class="p-green"></span><span class="p-yellow"></span><span class="p-blue"></span><span class="p-red"></span></div>
</section>

<section class="card card--front">
  <div class="wordmark"><span class="wordmark__square"></span>R.T. Custom Cabinets Ltd.</div>

  <div class="person">
    <h1 class="person__name">Daniel <strong>Marchetti</strong></h1>
    <p class="person__role">Owner/Business Manager</p>
  </div>

  <ul class="contacts">
    <li>
      <svg width="14" height="18" viewBox="0 0 14 18"><path d="M7 0a7 7 0 0 0-7 7c0 5 7 11 7 11s7-6 7-11a7 7 0 0 0-7-7zm0 10a3 3 0 1 1 0-6 3 3 0 0 1 0 6z"/></svg>
      <span>5826 Larkspur Avenue<br>Burnaby, B.C. V7K 2P9</span>
    </li>
    <li>
      <svg width="16" height="16" viewBox="0 0 16 16"><path d="M3.5 1l2.5 3-1.5 2a9 9 0 0 0 5 5l2-1.5 3 2.5-1.5 3C7 14.5 1.5 9 1 2.5z"/></svg>
      <span><span class="label">T</span> 604-555-0173</span>
    </li>
    <li>
      <svg width="16" height="16" viewBox="0 0 16 16"><path d="M4 0h8v5H4zM1 6h14v7h-3v3H4v-3H1zm5 6v2h4v-2z"/></svg>
      <span><span class="label">F</span> 604-555-0173</span>
    </li>
    <li>
      <svg width="18" height="14" viewBox="0 0 18 14"><path d="M1 1h16v12H1zM1.5 2.5 9 8l7.5-5.5" fill="none" stroke="#9bcb3c" stroke-width="1.8"/></svg>
      <span>daniel@rtcustomcabinets.example</span>
    </li>
  </ul>

  <div class="rule"></div>
  <p class="website">www.rtcustomcabinets.example</p>
</section>

</body>
</html>
```